Boutique sales recruiting firm needs dual purpose business card

We need a business card designed for a sales recruiting company called Brisk Otter Recruiting. We help both sales reps looking for work as well as companies looking for talent. What makes us unique is that 'we like to hunt', not literally but hunt for great companies and greats recruits. We are looking for a business card that on one side targets sales reps looking for work and on the other side companies looking for sales reps that incorporates the feel of a "Brisk Otter" as well as having dual personalities.

```html
<!DOCTYPE html>
<html lang="en">
<head>
<meta charset="utf-8">
<title>Brisk Otter Recruiting – Business Card</title>
<link href="https://fonts.googleapis.com/css2?family=Sora:wght@400;700&display=swap" rel="stylesheet">
<style>
  :root {
    --backdrop: #2b2b2b;
    --card: #f4f4f4;
    --ink: #0e1414;
    --accent: #e89a1c;
    --muted: #333333;
  }
  * { box-sizing: border-box; margin: 0; padding: 0; }
  html, body { width: 1200px; height: 1200px; overflow: hidden; }
  body {
    background: var(--backdrop);
    font-family: "Sora", sans-serif;
    display: flex;
    flex-direction: column;
    align-items: center;
    justify-content: center;
    gap: 70px;
  }
  .card {
    position: relative;
    width: 840px;
    height: 480px;
    background: linear-gradient(135deg, #ffffff 0%, var(--card) 60%, #e9e9e9 100%);
    box-shadow: 0 14px 30px rgba(0,0,0,.45);
  }
  .brand {
    position: absolute;
    display: flex;
    align-items: center;
    gap: 14px;
    color: var(--ink);
    font-weight: 700;
    letter-spacing: -1px;
    white-space: nowrap;
  }
  .brand-square { background: var(--ink); flex: none; }
  .card-front .brand { left: 260px; top: 180px; font-size: 64px; }
  .card-front .brand-square { width: 38px; height: 38px; }
  .card-back .brand { left: 470px; top: 90px; font-size: 48px; }
  .card-back .brand-square { width: 28px; height: 28px; }
  .identity { position: absolute; left: 70px; top: 110px; }
  .person-name { color: var(--accent); font-weight: 700; font-size: 30px; line-height: 1.1; }
  .person-title { color: var(--muted); font-size: 18px; margin-top: 6px; }
  .contacts { list-style: none; margin-top: 26px; }
  .contacts li {
    display: flex; align-items: center; gap: 10px;
    font-size: 18px; color: var(--muted); margin-bottom: 8px;
  }
  .contacts svg { width: 15px; height: 15px; flex: none; }
  .icon-fill { fill: var(--accent); }
  .icon-line { fill: none; stroke: var(--accent); stroke-width: 2.4; }
  .address {
    position: absolute; left: 520px; bottom: 60px;
    font-size: 20px; line-height: 1.45; color: var(--ink);
  }
</style>
</head>
<body>
  <section class="card card-front">
    <div class="brand"><span class="brand-square"></span>Brisk Otter</div>
  </section>

  <section class="card card-back">
    <div class="identity">
      <h1 class="person-name">Dana Whitfield</h1>
      <p class="person-title">Director &amp; CEO</p>
      <ul class="contacts">
        <li>
          <svg viewBox="0 0 24 24" aria-hidden="true"><path class="icon-fill" d="M6.6 10.8a15.1 15.1 0 0 0 6.6 6.6l2.2-2.2c.3-.3.7-.4 1-.2 1.1.4 2.3.6 3.6.6.6 0 1 .4 1 1V20c0 .6-.4 1-1 1A17 17 0 0 1 3 4c0-.6.4-1 1-1h3.5c.6 0 1 .4 1 1 0 1.3.2 2.5.6 3.6.1.3 0 .7-.2 1z"/></svg>
          905-555-0148
        </li>
        <li>
          <svg viewBox="0 0 24 24" aria-hidden="true"><rect class="icon-line" x="3" y="6" width="18" height="13"/><path class="icon-line" d="M3 6l9 7 9-7"/></svg>
          dana@briskotterrecruiting.com
        </li>
        <li>
          <svg viewBox="0 0 24 24" aria-hidden="true"><circle class="icon-fill" cx="12" cy="12" r="10"/></svg>
          www.briskotterrecruiting.com
        </li>
      </ul>
    </div>
    <div class="brand"><span class="brand-square"></span>Brisk Otter</div>
    <p class="address">48 Harbourview Lane,<br>Oakridge, ON K2P 3M7</p>
  </section>
</body>
</html>
```